Boutique Salon Brand Refresh needs color palette, font, templates.

Lorvu Hair Design is an established hair salon celebrating 10 years in business. We are currently evolving our brand to better reflect who we are today, the clients we serve, and the direction we want to take our business moving forward.
Our goal is to position Lorvu as a refined, modern boutique salon created specifically for “The Lorvu Woman.”
In the past, much of our branding and marketing focused on us—our salon, our space, our services, and our team. Going forward, we want to shift that focus to her: who she is, what she values, how she wants to look and feel, and how Lorvu fits into her life.
We want our brand to communicate expertise and quality without feeling overly luxurious, trendy, intimidating, or impersonal. It should feel polished, sophisticated, warm, approachable, and timeless—a boutique experience designed for women who value beautiful, healthy hair and trusted professional guidance.
As part of this rebrand, we are looking to establish a cohesive visual identity that can be carried consistently across our website, social media, email marketing, print materials, signage, and other client touchpoints.

*** For THIS PROJECT, we are SPECIFICALLY LOOKING for:
- A cohesive brand color palette
- 2–3 complementary fonts for consistent use across our marketing
- 4–5 customizable social media templates that can be used across Instagram and Facebook
A visual direction that feels distinctive to Lorvu and speaks directly to The Lorvu Woman.
The following information provides more detail about The Lorvu Woman, our positioning, brand personality, values, and the overall direction we envision for the next chapter of Lorvu Hair Design.
Lorvu Hair Design
Mendham, NJ USA
lorvuhairstudio.example

--PRIMARY AUDIENCE
The Lorvu woman values quality, consistency, and professional guidance.
She wants to look polished and current without appearing overdone or overly trendy.
She may be managing grey hair, changing texture, thinning, dryness, fading color, or a style that no longer reflects who she is. She wants an expert who understands these concerns and can create a realistic plan.
She is willing to invest in professional services and products when she understands their value.
She does not want to experiment with her appearance.
She wants to feel confident in the person caring for her hair.
Women approximately 45 to 65 years old living in Mendham, Morris County, and surrounding communities.

--COLOR PALETTE
The overall appearance should feel calm, spacious, editorial, and cohesive. The entire visual system should feel more like a refined boutique hotel, skincare brand, or luxury lifestyle publication than a traditional salon advertisement.
When choosing the palette, we want the colors to invoke these feelings.
Represents:
Expertise
Confidence
Timelessness
Professionalism
Calm
Warmth
Cleanliness
Soft luxury
Natural beauty
Warmth
Balance
Subtle sophistication
Consistency

--TYPOGRAPHY
The typography system should feel refined, modern, readable, and timeless.
Recommended usage for each font, size, spacing, etc.

----TEMPLATE IDEAS
**EDUCATIONAL POST
Frequently asked questions
Healthy-hair advice
Healthy Hair Tip
Grey Coverage FAQ
Grey Blending FAQ
Product education
Single-tip graphic
**REVIEWS
Google reviews
Finest in Town recognition/Community awards
Long-term guest relationships
Guest testimonials/satisfaction stories
Referral stories
**ADS
**SALON UPDATES/INFO
Holiday hours
Policy reminder
New guest guide
Consultation invitation
Service spotlight
Seasonal guidance
**ABOUT LORVU
Who we are
What to expect from us
What we can provide
Our expertise
**HIGHLIGHT ICON
Questions
Testimonial
Product
Reminders

TEMPLATE RULES
Use the color palette
Use only the font system
Maintain generous spacing
Limit text
Use consistent margins
Keep calls to action simple
Avoid crowded layouts
Use photography intentionally
Keep every template recognizably Lorvu

Target Market(s)

Women approximately 45 to 65 years old living in Mendham, Morris County, and surrounding communities. She values quality, consistency, and professional guidance. She wants to look polished and current without appearing overdone or overly trendy. She is willing to invest in professional services and products when she understands their value.

Industry/Entity Type

Hair Salon

Font styles to use
Serif
Sans Serif
Script

Requirements
Must have
• We are looking to establish a cohesive visual identity that can be carried consistently across platforms. It should communicate expertise and quality without feeling overly fluffy, trendy, intimidating, or impersonal. I would like to see multiple template ideas. Example- one template for education post, one template for reviews, one for salon information/updates. etc. My main goal here is to simplify social media posts by having designated templates for each post category. WE WILL BE KEEPING OUR ORGINAL LOGO- SO COLOR PALETTE MUST REFLECT THAT.
Nice to have
• Color palette and font sets that reflect the brand. **cohesive visual identity**
Should not have
• Nothing flashy, busy, overly trendy.

```html
<!DOCTYPE html>
<html lang="en">
<head>
<meta charset="utf-8">
<title>Lorvu Hair Design — Frequently Asked</title>
<link rel="stylesheet" href="https://fonts.googleapis.com/css2?family=Playfair+Display:wght@400&family=Jost:ital,wght@0,400;0,500;0,600;1,600&display=swap">
<style>
  :root {
    --paper: #f7f6f3;
    --crimson: #c00033;
    --ink: #111111;
    --white: #ffffff;
  }
  html, body {
    margin: 0;
    padding: 0;
    width: 1200px;
    height: 1200px;
    overflow: hidden;
    background: var(--paper);
  }
  .post {
    position: relative;
    width: 1200px;
    height: 1200px;
    background: var(--paper);
    overflow: hidden;
    font-family: "Jost", sans-serif;
    color: var(--ink);
  }
  .brand-panel {
    position: absolute;
    inset: 0;
    width: 1200px;
    height: 1200px;
  }
  .corner-photo {
    position: absolute;
    left: 0;
    top: 0;
    width: 212px;
    height: 212px;
  }
  .brand-name {
    position: absolute;
    left: 860px;
    top: 150px;
    width: 270px;
    margin: 0;
    color: var(--white);
    font-family: "Jost", sans-serif;
    font-weight: 400;
    font-size: 84px;
    line-height: 1;
    text-align: center;
  }
  .headline {
    position: absolute;
    left: 88px;
    top: 228px;
    margin: 0;
    font-family: "Playfair Display", serif;
    font-weight: 400;
    font-size: 81px;
    line-height: 94px;
    color: var(--crimson);
    letter-spacing: -1px;
  }
  .faq {
    position: absolute;
    left: 96px;
    top: 434px;
    width: 680px;
  }
  .faq-row {
    display: grid;
    grid-template-columns: 40px 1fr;
    margin: 0;
  }
  .faq-label { font-weight: 600; font-size: 30px; }
  .faq-question {
    font-weight: 600;
    font-size: 30.5px;
    line-height: 36px;
    margin-left: 9px;
    white-space: nowrap;
  }
  .faq-answer-row { margin-top: 12px; }
  .faq-answer {
    font-weight: 400;
    font-size: 30.5px;
    line-height: 41.3px;
    margin: -4px 0 0 0;
    white-space: nowrap;
  }
  .cta {
    position: absolute;
    left: 84px;
    top: 965px;
    width: 1008px;
    height: 74px;
    border-radius: 37px;
    background: var(--ink);
    color: var(--white);
    font-style: italic;
    font-weight: 600;
    font-size: 49px;
    line-height: 72px;
    text-align: center;
    margin: 0;
  }
  .web {
    position: absolute;
    left: 144px;
    top: 1068px;
    display: flex;
    align-items: center;
    gap: 8px;
    font-size: 32px;
  }
  .web svg { width: 36px; height: 36px; }
  .product-photo {
    position: absolute;
    left: 1040px;
    top: 960px;
    width: 160px;
    height: 240px;
  }
</style>
</head>
<body>
<main class="post">
  <svg class="brand-panel" viewBox="0 0 1200 1200" aria-hidden="true">
    <defs>
      <linearGradient id="crimsonFill" x1="0" y1="0" x2="1" y2="1">
        <stop offset="0" stop-color="#c30036"/>
        <stop offset="0.5" stop-color="#b8002f"/>
        <stop offset="1" stop-color="#c4063a"/>
      </linearGradient>
    </defs>
    <polygon fill="url(#crimsonFill)" points="
      774,0 1200,0 1200,1200 762,1200 768,1170 760,1140 770,1110 764,1080 772,1050 766,1010
      776,975 770,940 780,905 774,870 786,835 778,800 790,765 782,730 792,695 784,660
      794,625 786,590 796,555 788,520 795,485 786,450 792,415 784,380 790,345 782,310
      788,275 778,240 784,205 774,170 780,135 770,100 778,65 768,30"/>
  </svg>

  <svg class="corner-photo" viewBox="0 0 212 212" role="img" aria-label="Close-up photograph of a salon styling tool">
    <defs>
      <radialGradient id="cornerTone" cx="0.35" cy="0.35" r="0.7">
        <stop offset="0" stop-color="#9a9a9a"/>
        <stop offset="0.6" stop-color="#d9d9d9"/>
        <stop offset="1" stop-color="#f7f6f3"/>
      </radialGradient>
    </defs>
    <path d="M0,0 H210 A210,210 0 0 1 0,210 Z" fill="url(#cornerTone)"/>
    <path d="M210,0 A210,210 0 0 1 0,210" fill="none" stroke="#c00033" stroke-width="3"/>
  </svg>

  <p class="brand-name">Lorvu</p>

  <h1 class="headline">FREQUENTLY<br>ASKED</h1>

  <section class="faq">
    <p class="faq-row">
      <span class="faq-label">Q:</span>
      <span class="faq-question">How do I know which color service<br>is right for me?</span>
    </p>
    <div class="faq-row faq-answer-row">
      <span class="faq-label">A:</span>
      <p class="faq-answer">It starts with a consultation. Our stylists<br>take the time to understand your hair<br>history, lifestyle, maintenance preferences,<br>and desired result before recommending a<br>service. Whether you're looking to refresh<br>your color, add dimension, brighten your<br>hair, or blend your natural gray, we'll help<br>you find an approach that feels realistic<br>and right for you.</p>
    </div>
  </section>

  <svg class="product-photo" viewBox="0 0 160 240" role="img" aria-label="Soft-focus photograph of a hair care product">
    <defs>
      <radialGradient id="productTone" cx="0.7" cy="0.55" r="0.6">
        <stop offset="0" stop-color="#8e8e8e"/>
        <stop offset="0.55" stop-color="#c9c9c9" stop-opacity="0.8"/>
        <stop offset="1" stop-color="#c00033" stop-opacity="0"/>
      </radialGradient>
    </defs>
    <rect width="160" height="240" fill="url(#productTone)"/>
  </svg>

  <p class="cta">Let’s create a plan for your hair.</p>

  <div class="web">
    <svg viewBox="0 0 36 36" aria-hidden="true">
      <g fill="none" stroke="#c00033" stroke-width="2.4">
        <circle cx="18" cy="18" r="15"/>
        <ellipse cx="18" cy="18" rx="6.5" ry="15"/>
        <line x1="3" y1="18" x2="33" y2="18"/>
        <line x1="5.5" y1="10" x2="30.5" y2="10"/>
        <line x1="5.5" y1="26" x2="30.5" y2="26"/>
      </g>
    </svg>
    <span>lorvuhairstudio.example</span>
  </div>
</main>
</body>
</html>
```